Amazing Website for innovative Tax-App

Background:
Our Company "Rendolo" provides all employees an App, that allows them to file their tax easy, in only a few minutes and most importantly without any prior knowledge. Most people miss out on their well deserved tax refund. Rendolo helps these people to not only get back their money, but also to maximise their refund.
Task:
Please help us create a beautiful and high quality Webdesign with breathtaking mockups, which immediately reflects what rendolo stands for.
Rendolo is THE tool for getting back tax money (could have a slightly official government touch)
Rendolo breaks down complex old procedures in the utmost easiest way, so that filing your tax via app with a few clicks becomes almost fun.
Additional:
Please surprise us with great mockups, that showcases our app, maybe some icons that reflects users individual life and flying around. (Taxes are as individual as users life!
Maybe catch people with a notification that shows that in your online banking you got around 1000€ in refund and create excitement that "you could be the next"
Work with the newest iphone devices as mockup and use screenshots that are provided in files. You can also think of creating some 3D elements around the phone.
this is how our current website looks like: www.rendolo-beispiel.at
You can take inspirations from that existing site.
Plus, this is is a website from another company in the same field that we like: https://www.kassmiro-beispiel.com/
Please provide complete desktop and mobile website Design and most importantly..
Please be creative!

```html
<!DOCTYPE html>
<html lang="en">
<head>
<meta charset="utf-8">
<title>Rendolo – Website Design Overview</title>
<link rel="stylesheet" href="https://fonts.googleapis.com/css2?family=Poppins:wght@400;500;600;700&display=swap">
<style>
  :root {
    --teal: #1cbfa6;
    --teal-dark: #13a38d;
    --teal-light: #3fe0c6;
    --ink: #16211f;
    --text: #4a4f4e;
    --muted: #8a8f8e;
    --page: #ffffff;
    --board: #f5f5f5;
    --section: #f8f8f8;
    --blob: #ececec;
    --star: #f6b71c;
    --press-blue: #2a5a8c;
  }
  * { box-sizing: border-box; margin: 0; padding: 0; }
  html, body { width: 1200px; height: 1161px; overflow: hidden; }
  body { font-family: "Poppins", sans-serif; background: var(--board); color: var(--ink); position: relative; }

  .t { position: absolute; white-space: nowrap; line-height: 1.2; }
  .c { transform: translateX(-50%); text-align: center; }
  .accent { color: var(--teal); }
  .box { position: absolute; }

  /* ---------- desktop page ---------- */
  .desktop-page { position: absolute; left: 38.6px; top: 177px; width: 1231px; height: 1608px; transform: scale(.6122); transform-origin: 0 0; background: var(--page); overflow: hidden; box-shadow: 0 0 60px rgba(0,0,0,.06); }
  .desktop-page .how-band { position: absolute; left: 0; top: 788px; width: 1231px; height: 578px; background: var(--section); }
  .desktop-page .brand { position: absolute; left: 91px; top: 38px; display: flex; align-items: center; gap: 14px; font-size: 38px; font-weight: 500; color: var(--teal); line-height: 1; }
  .desktop-page .brand-mark { width: 40px; height: 40px; border-radius: 10px; background: var(--teal); }
  .desktop-page .nav { font-size: 15px; color: var(--text); top: 47px; }
  .desktop-page .btn-login { position: absolute; left: 899px; top: 40px; width: 106px; height: 34px; border-radius: 17px; background: var(--teal); color: #fff; font-size: 15px; display: flex; align-items: center; justify-content: center; }
  .desktop-page .hero-title { font-size: 48px; font-weight: 600; }
  .desktop-page .hero-lead { font-size: 15px; color: var(--text); }
  .store-btn { position: absolute; display: flex; align-items: center; border-radius: 999px; color: #fff; }
  .store-btn.dark { background: #0e0e0e; }
  .store-btn.light { background: var(--teal); }
  .store-btn .dot { border-radius: 50%; background: #fff; flex: none; }
  .store-btn small { display: block; line-height: 1; }
  .store-btn strong { display: block; font-weight: 500; line-height: 1.15; }
  .desktop-page .store-btn { height: 39px; padding: 0 14px; gap: 9px; }
  .desktop-page .store-btn .dot { width: 18px; height: 18px; }
  .desktop-page .store-btn small { font-size: 8px; }
  .desktop-page .store-btn strong { font-size: 14px; }
  .stars { color: var(--star); letter-spacing: 1px; }
  .blob { position: absolute; border-radius: 48% 52% 45% 55%; background: radial-gradient(circle at 50% 45%, #f6f6f6, var(--blob)); }
  .phone-area { position: absolute; background: linear-gradient(160deg, #5fc4ae, #3aae97 60%, #e9f5f2); box-shadow: 0 24px 40px rgba(0,0,0,.14); }
  .cube { position: absolute; background: linear-gradient(145deg, var(--teal-light), var(--teal-dark)); }
  .desktop-page .press { top: 705px; font-size: 26px; font-weight: 700; color: #222; }
  .desktop-page .label { font-size: 15px; font-weight: 600; letter-spacing: 3px; color: #2a2a2a; }
  .desktop-page .section-title { font-size: 44px; font-weight: 600; }
  .desktop-page .step-text { font-size: 16px; color: var(--muted); line-height: 1.35; }
  .desktop-page .feature-card { position: absolute; top: 1596px; height: 60px; background: #fff; box-shadow: 0 0 24px rgba(0,0,0,.05); }
  .layer { position: absolute; left: 0; top: 0; }

  /* ---------- full page overview ---------- */
  .overview { position: absolute; left: 822.2px; top: 40.4px; width: 443px; height: 1742px; transform: scale(.6122); transform-origin: 0 0; background: var(--page); overflow: hidden; box-shadow: 0 0 40px rgba(0,0,0,.08); }
  .overview .band-grey { position: absolute; left: 0; width: 443px; background: var(--section); }
  .overview .band-start { position: absolute; left: 0; top: 724px; width: 443px; height: 187px; background: linear-gradient(180deg, #fff 0%, #fff 40%, #e2f7f3 100%); }
  .overview .brand { position: absolute; left: 32px; top: 13px; display: flex; align-items: center; gap: 4px; font-size: 13px; font-weight: 500; color: var(--teal); line-height: 1; }
  .overview .brand-mark { width: 13px; height: 13px; border-radius: 3px; background: var(--teal); }
  .overview .nav { font-size: 5px; color: var(--text); top: 17px; }
  .overview .pill { position: absolute; border-radius: 999px; display: flex; align-items: center; justify-content: center; }
  .overview .h-title { font-size: 17px; font-weight: 600; }
  .overview .tiny { font-size: 4.5px; color: var(--text); }
  .overview .micro { font-size: 3.6px; color: var(--muted); line-height: 1.45; }
  .overview .store-btn { height: 15px; padding: 0 5px; gap: 3px; }
  .overview .store-btn .dot { width: 6px; height: 6px; }
  .overview .store-btn small { font-size: 2.5px; }
  .overview .store-btn strong { font-size: 4.5px; }
  .overview .press { top: 254px; font-size: 8px; font-weight: 700; color: #222; }
  .overview .sec-title { font-size: 15px; font-weight: 600; }
  .overview .card { position: absolute; background: #fff; box-shadow: 0 2px 10px rgba(0,0,0,.07); }
  .overview .card-btn { position: absolute; left: 0; bottom: 0; width: 100%; height: 16px; background: var(--teal); color: #fff; font-size: 3.5px; display: flex; align-items: center; justify-content: center; }
  .overview .card-icon { position: absolute; top: 16px; left: 50%; width: 20px; height: 20px; margin-left: -10px; border-radius: 50%; border: 1.5px solid var(--teal); }
  .overview .card-title { position: absolute; top: 43px; width: 100%; text-align: center; font-size: 5px; font-weight: 600; }
  .overview .card-body { position: absolute; top: 56px; left: 6px; right: 6px; text-align: center; font-size: 3.4px; line-height: 1.5; color: var(--muted); }
  .overview .review { position: absolute; width: 124px; background: #fff; box-shadow: 0 2px 10px rgba(0,0,0,.06); padding: 14px 10px 0 10px; }
  .overview .review h4 { font-size: 5px; font-weight: 600; color: var(--teal); }
  .overview .review p { font-size: 3.4px; line-height: 1.45; color: var(--text); margin-top: 3px; width: 86px; }
  .overview .review .quote { position: absolute; right: 8px; top: 6px; font-size: 26px; line-height: 1; color: #e6e6e6; font-weight: 700; }
  .overview .review .who { display: flex; align-items: center; gap: 4px; margin-top: 6px; font-size: 3.6px; font-weight: 600; }
  .overview .review .avatar { width: 12px; height: 12px; border-radius: 50%; background: #b9bcbb; }
  .overview .review .stars { font-size: 4px; margin-left: auto; }
  .overview .ico { position: absolute; width: 7px; height: 7px; border-radius: 50%; background: var(--teal); }
  .overview .foot { font-size: 4px; color: var(--muted); }
  .overview .foot-h { font-size: 5px; font-weight: 600; color: var(--ink); }
</style>
</head>
<body>

<!-- ================= desktop page ================= -->
<main class="desktop-page">
  <div class="how-band"></div>

  <div class="brand"><span class="brand-mark"></span>rendolo</div>
  <span class="t nav" style="left:557px;">Our Vision</span>
  <span class="t nav" style="left:657px;">Advantages</span>
  <span class="t nav" style="left:771px;">How it Works</span>
  <span class="btn-login">Log In</span>
  <span class="t nav" style="left:1061px;">English</span>

  <h1 class="t hero-title" style="left:91px;top:206px;">You Could Be</h1>
  <h1 class="t hero-title accent" style="left:91px;top:268px;">The Next</h1>
  <p class="t hero-lead" style="left:91px;top:359px;">+50,000 employee assessments</p>
  <p class="t hero-lead" style="left:91px;top:385px;">have already been created with the help of Rendolo</p>

  <div class="store-btn dark" style="left:91px;top:438px;"><span class="dot"></span><div><small>Download in</small><strong>AppHafen</strong></div></div>
  <div class="store-btn light" style="left:226px;top:438px;"><span class="dot"></span><div><small>Now In</small><strong>Playmarkt</strong></div></div>

  <div class="t" style="left:91px;top:514px;display:flex;align-items:center;gap:8px;font-size:10px;color:var(--text);">
    <span style="width:16px;height:16px;border-radius:50%;background:var(--teal);"></span>
    <span class="stars" style="font-size:13px;">★★★★★</span>
    <span>2000+Reviews on Bewertio</span>
  </div>

  <div class="box" role="img" aria-label="Smartphone showing a refund result of 861,70 € with floating 3D app tiles" style="left:0;top:0;width:1231px;height:680px;">
    <div class="blob" style="left:642px;top:91px;width:492px;height:560px;"></div>
    <div class="phone-area" style="left:770px;top:190px;width:190px;height:400px;border-radius:36px;transform:rotate(30deg);"></div>
    <div class="cube" style="left:1036px;top:112px;width:76px;height:76px;border-radius:22px;transform:rotate(12deg);"></div>
    <div class="cube" style="left:580px;top:405px;width:112px;height:112px;border-radius:30px;transform:rotate(-18deg);"></div>
  </div>

  <span class="t c" style="left:615px;top:638px;font-size:18px;color:var(--muted);">Known From</span>
  <span class="t c press" style="left:176px;">Ledgerline</span>
  <span class="t c press" style="left:400px;">Abendblick</span>
  <span class="t c press" style="left:608px;">Kapitalo</span>
  <span class="t c press" style="left:830px;color:var(--press-blue);">Marktweise</span>
  <span class="t c press" style="left:1065px;">Themenwelle</span>

  <span class="t c label" style="left:615px;top:860px;">HOW IT WORKS</span>
  <h2 class="t c section-title" style="left:615px;top:918px;">Your Tax Offset <span class="accent">Done Quickly</span></h2>

  <svg class="layer" width="1231" height="1608" viewBox="0 0 1231 1608">
    <g fill="none" stroke="var(--teal)" stroke-width="2">
      <path d="M90 1146 A132 132 0 0 1 354 1146"/>
      <path d="M354 1146 A132 132 0 0 0 618 1146"/>
      <path d="M618 1146 A132 132 0 0 1 881 1146"/>
      <path d="M881 1146 A132 132 0 0 0 1144 1146"/>
    </g>
    <g fill="var(--teal)">
      <circle cx="90" cy="1146" r="5"/><circle cx="354" cy="1146" r="5"/><circle cx="618" cy="1146" r="5"/><circle cx="881" cy="1146" r="5"/><circle cx="1144" cy="1146" r="5"/>
    </g>
    <g fill="#fff" style="filter:drop-shadow(0 10px 22px rgba(0,0,0,.06))">
      <circle cx="222" cy="1144" r="105"/><circle cx="486" cy="1144" r="105"/><circle cx="749" cy="1144" r="105"/><circle cx="1012" cy="1144" r="105"/>
    </g>
    <g fill="var(--teal)">
      <circle cx="222" cy="1108" r="31"/><circle cx="486" cy="1108" r="31"/><circle cx="749" cy="1108" r="31"/><circle cx="1012" cy="1108" r="31"/>
    </g>
    <g stroke="#fff" stroke-width="2.6" fill="none" stroke-linecap="round" stroke-linejoin="round">
      <path transform="translate(222 1108)" d="M0 -13 V5 M-8 -2 L0 6 L8 -2 M-10 11 H10"/>
      <path transform="translate(749 1108)" d="M0 -14 L4 -6 L13 -5 L6 1 L8 10 L0 5 L-8 10 L-6 1 L-13 -5 L-4 -6 Z"/>
      <path transform="translate(1012 1108)" d="M-7 13 V-13 H10 L6 -7 L10 -1 H-7"/>
    </g>
    <g fill="#fff"><circle cx="475" cy="1108" r="3.6"/><circle cx="486" cy="1108" r="3.6"/><circle cx="497" cy="1108" r="3.6"/></g>
  </svg>

  <p class="t c step-text" style="left:222px;top:1158px;">Download<br>Rendolo App</p>
  <p class="t c step-text" style="left:486px;top:1158px;">Answer Simple<br>Questions</p>
  <p class="t c step-text" style="left:749px;top:1158px;">Find Out The<br>Result Immediately</p>
  <p class="t c step-text" style="left:1012px;top:1158px;">Send To The Tax Office<br>With One Click</p>

  <h2 class="t c section-title" style="left:605px;top:1441px;">The <span class="accent">Super App</span> For Taxes</h2>
  <div class="feature-card" style="left:27px;width:340px;"></div>
  <div class="feature-card" style="left:482px;width:250px;"></div>
  <div class="feature-card" style="left:842px;width:255px;"></div>
</main>

<!-- ================= full page overview ================= -->
<section class="overview">
  <div class="band-grey" style="top:282px;height:209px;"></div>
  <div class="band-start"></div>
  <div class="band-grey" style="top:1606px;height:136px;"></div>

  <div class="brand"><span class="brand-mark"></span>rendolo</div>
  <span class="t nav" style="left:200px;">Our Vision</span>
  <span class="t nav" style="left:235px;">Advantages</span>
  <span class="t nav" style="left:277px;">How it Works</span>
  <span class="pill" style="left:323px;top:14px;width:38px;height:12px;background:var(--teal);color:#fff;font-size:4.5px;">Log In</span>
  <span class="t nav" style="left:381px;">English</span>

  <span class="t h-title" style="left:32px;top:73px;">You Could Be</span>
  <span class="t h-title accent" style="left:32px;top:96px;">The Next</span>
  <span class="t tiny" style="left:32px;top:129px;">+50,000 employee assessments</span>
  <span class="t tiny" style="left:32px;top:138px;">have already been created with the help of Rendolo</span>
  <div class="store-btn dark" style="left:32px;top:157px;"><span class="dot"></span><div><small>Download in</small><strong>AppHafen</strong></div></div>
  <div class="store-btn light" style="left:81px;top:157px;"><span class="dot"></span><div><small>Now In</small><strong>Playmarkt</strong></div></div>
  <span class="t tiny" style="left:32px;top:184px;font-size:3.5px;"><span class="stars" style="font-size:4.5px;">★★★★★</span> 2000+Reviews on Bewertio</span>

  <div class="box" role="img" aria-label="Smartphone showing a refund result with floating 3D app tiles" style="left:0;top:0;width:443px;height:240px;">
    <div class="blob" style="left:230px;top:34px;width:179px;height:200px;"></div>
    <div class="phone-area" style="left:278px;top:66px;width:66px;height:150px;border-radius:13px;transform:rotate(30deg);"></div>
    <div class="cube" style="left:372px;top:41px;width:27px;height:27px;border-radius:8px;transform:rotate(12deg);"></div>
    <div class="cube" style="left:208px;top:147px;width:40px;height:40px;border-radius:11px;transform:rotate(-18deg);"></div>
  </div>
  <span class="t tiny" style="left:202px;top:230px;color:var(--muted);">Known From</span>
  <span class="t c press" style="left:63px;">Ledgerline</span>
  <span class="t c press" style="left:144px;">Abendblick</span>
  <span class="t c press" style="left:218px;">Kapitalo</span>
  <span class="t c press" style="left:299px;color:var(--press-blue);">Marktweise</span>
  <span class="t c press" style="left:383px;">Themenwelle</span>

  <span class="t c" style="left:221px;top:310px;font-size:4.5px;font-weight:600;letter-spacing:1px;">HOW IT WORKS</span>
  <span class="t c sec-title" style="left:221px;top:331px;">Your Tax Offset <span class="accent">Done Quickly</span></span>

  <svg class="layer" width="443" height="1742" viewBox="0 0 443 1742">
    <g fill="none" stroke="var(--teal)" stroke-width="1">
      <path d="M32 408 A47.5 47.5 0 0 1 127 408"/>
      <path d="M127 408 A47.5 47.5 0 0 0 222 408"/>
      <path d="M222 408 A47.5 47.5 0 0 1 317 408"/>
      <path d="M317 408 A47.5 47.5 0 0 0 412 408"/>
    </g>
    <g fill="var(--teal)"><circle cx="32" cy="408" r="1.8"/><circle cx="127" cy="408" r="1.8"/><circle cx="222" cy="408" r="1.8"/><circle cx="317" cy="408" r="1.8"/><circle cx="412" cy="408" r="1.8"/></g>
    <g fill="#fff" style="filter:drop-shadow(0 3px 6px rgba(0,0,0,.06))">
      <circle cx="79" cy="406" r="38"/><circle cx="174" cy="406" r="38"/><circle cx="269" cy="406" r="38"/><circle cx="364" cy="406" r="38"/>
    </g>
    <g fill="var(--teal)"><circle cx="79" cy="399" r="11"/><circle cx="174" cy="399" r="11"/><circle cx="269" cy="399" r="11"/><circle cx="364" cy="399" r="11"/></g>
    <g stroke="#fff" stroke-width="1.1" fill="none" stroke-linecap="round" stroke-linejoin="round">
      <path transform="translate(79 399) scale(.38)" d="M0 -13 V5 M-8 -2 L0 6 L8 -2 M-10 11 H10"/>
      <path transform="translate(269 399) scale(.38)" d="M0 -14 L4 -6 L13 -5 L6 1 L8 10 L0 5 L-8 10 L-6 1 L-13 -5 L-4 -6 Z"/>
      <path transform="translate(364 399) scale(.38)" d="M-7 13 V-13 H10 L6 -7 L10 -1 H-7"/>
    </g>
    <g fill="#fff"><circle cx="170" cy="399" r="1.3"/><circle cx="174" cy="399" r="1.3"/><circle cx="178" cy="399" r="1.3"/></g>
    <g fill="none" stroke="var(--teal)" stroke-width="1"><circle cx="92" cy="1074" r="9" stroke="#ddd"/></g>
    <circle cx="118" cy="1074" r="9" fill="var(--teal)"/>
    <g stroke-width="1" fill="none" stroke-linecap="round">
      <path d="M96 1074 H88 M91 1071 L88 1074 L91 1077" stroke="#333"/>
      <path d="M114 1074 H122 M119 1071 L122 1074 L119 1077" stroke="#fff"/>
    </g>
  </svg>
  <span class="t c micro" style="left:79px;top:418px;">Download<br>Rendolo App</span>
  <span class="t c micro" style="left:174px;top:418px;">Answer Simple<br>Questions</span>
  <span class="t c micro" style="left:269px;top:418px;">Find Out The<br>Result Immediately</span>
  <span class="t c micro" style="left:364px;top:418px;">Send To The Tax Office<br>With One Click</span>

  <span class="t c sec-title" style="left:221px;top:520px;">The <span class="accent">Super App</span> For Taxes</span>

  <div class="card" style="left:40px;top:572px;width:92px;height:134px;">
    <span class="card-icon"></span><span class="card-title">Simply</span>
    <p class="card-body">Everything is simple with us. Rendolo guides you through all relevant questions and sends it all digitally with a click.</p>
    <span class="card-btn">View More →</span>
  </div>
  <div class="card" style="left:172px;top:572px;width:91px;height:134px;">
    <span class="card-icon"></span><span class="card-title">Secure</span>
    <p class="card-body">Rendolo is safe for you. We treat your information as strictly confidential and send it only to the tax office.</p>
    <span class="card-btn">View More →</span>
  </div>
  <div class="card" style="left:303px;top:572px;width:91px;height:134px;">
    <span class="card-icon"></span><span class="card-title">€0 cost risk</span>
    <p class="card-body">Rendolo is risk-free for you. No fees, no subscriptions. Only if you receive money back do we receive a fee.</p>
    <span class="card-btn">View More →</span>
  </div>

  <span class="t" style="left:30px;top:745px;font-size:15px;font-weight:600;">Start <span class="accent">Now</span>.</span>
  <span class="t" style="left:30px;top:772px;font-size:6px;line-height:1.9;">Test The Super Tax App Now And Find Out How<br>Much You Can Be Entitled To!</span>
  <span class="pill" style="left:30px;top:813px;width:59px;height:14px;background:var(--teal);color:#fff;font-size:4px;">Download App</span>
  <span class="t micro" style="left:45px;top:847px;color:var(--text);">Reliable and secure: highest<br>security standards</span>
  <span class="t micro" style="left:148px;top:847px;color:var(--text);">Popular mobile tax app<br>+ 300.000 downloads</span>
  <span class="t micro" style="left:45px;top:867px;color:var(--text);">Rank 1 of finance apps in the AppHafen ranking<br>(early 2023)</span>
  <span class="box" style="left:34px;top:849px;width:7px;height:7px;border:1px solid #555;border-radius:2px;"></span>
  <span class="box" style="left:135px;top:849px;width:7px;height:7px;border:1px solid #555;border-radius:50%;"></span>
  <span class="box" style="left:34px;top:869px;width:7px;height:7px;border:1px solid #555;border-radius:2px;"></span>
  <div class="box" role="img" aria-label="Photo of a smiling young man in a white shirt on a city street" style="left:224px;top:759px;width:188px;height:105px;background:linear-gradient(90deg,#3b4148,#7a8088 55%,#c9c6c0);"></div>
  <div class="cube" style="left:218px;top:831px;width:46px;height:46px;border-radius:13px;transform:rotate(-18deg);"></div>

  <span class="t" style="left:82px;top:958px;font-size:20px;font-weight:600;">4.8/5.0</span>
  <span class="t" style="left:82px;top:996px;font-size:12px;font-weight:600;line-height:1.55;">Hundreds Of <span class="accent">Thousands</span><br><span class="accent">Uesrs Trust Us.</span></span>
  <span class="t micro" style="left:82px;top:1036px;">Short review text from happy users<br>of the Rendolo tax app.</span>

  <div class="review" style="left:246px;top:989px;height:88px;"><span class="quote">“</span><h4>Lorem Ipsum text</h4><p>Filing my taxes took only a few minutes and the refund was higher than expected.</p><div class="who"><span class="avatar" role="img" aria-label="Reviewer portrait"></span>Jonas Berger<span class="stars">★★★★★</span></div></div>
  <div class="review" style="left:81px;top:1099px;height:86px;"><span class="quote">“</span><h4>Lorem Ipsum text</h4><p>Filing my taxes took only a few minutes and the refund was higher than expected.</p><div class="who"><span class="avatar" role="img" aria-label="Reviewer portrait"></span>Jonas Berger<span class="stars">★★★★★</span></div></div>
  <div class="review" style="left:246px;top:1099px;height:86px;"><span class="quote">“</span><h4>Lorem Ipsum text</h4><p>Filing my taxes took only a few minutes and the refund was higher than expected.</p><div class="who"><span class="avatar" role="img" aria-label="Reviewer portrait"></span>Jonas Berger<span class="stars">★★★★★</span></div></div>

  <div class="box" style="left:60px;top:1241px;width:323px;height:59px;border-radius:4px;background:linear-gradient(90deg,var(--teal),#22dcc4);"></div>
  <span class="t" style="left:92px;top:1253px;font-size:13px;font-weight:600;color:#fff;">Start now .</span>
  <span class="t" style="left:92px;top:1274px;font-size:4px;color:#fff;line-height:1.5;">Test the super tax app now and find out<br>how much you can be entitled to!</span>
  <span class="pill" style="left:275px;top:1266px;width:60px;height:13px;background:#fff;color:var(--teal);font-size:4px;">Download App</span>

  <div class="box" style="left:94px;top:1337px;width:93px;height:142px;background:#ececec;"></div>
  <div class="box" role="img" aria-label="Portrait photo of the founder in a white shirt" style="left:103px;top:1327px;width:101px;height:142px;background:linear-gradient(160deg,#5a4a3c,#a89a8c 55%,#e8e4de);"></div>
  <span class="t" style="left:235px;top:1357px;font-size:5px;color:var(--muted);">Austria's simplest tax equalization</span>
  <span class="t" style="left:235px;top:1375px;font-size:15px;font-weight:600;">Our <span class="accent">Vision</span></span>
  <span class="t micro" style="left:235px;top:1400px;">Our goal is to provide everyone living in Austria with<br>a targeted and simple path to their tax<br>compensation.</span>
  <span class="pill" style="left:235px;top:1436px;width:58px;height:15px;border:1px solid var(--teal);color:var(--teal);font-size:4px;font-weight:600;">SIGN UP</span>

  <div class="box" role="img" aria-label="Montage of tilted app screens in teal and white" style="left:0;top:1500px;width:443px;height:106px;background:linear-gradient(180deg,#ffffff 0%,#bfeee5 45%,#2fc7ae 100%);"></div>

  <span class="t micro" style="left:30px;top:1662px;">Short text about the Rendolo tax app<br>and how it helps employees get a<br>well deserved refund every year.</span>
  <span class="t micro" style="left:30px;top:1700px;">© Rendolo · All Rights Reserved</span>
  <span class="t foot-h" style="left:159px;top:1643px;">Quick Link</span>
  <span class="t foot" style="left:159px;top:1656px;line-height:3;">Home<br>Our Vision<br>Services<br>How it Works<br>Blogs</span>
  <span class="t foot-h" style="left:224px;top:1643px;">Contact Us</span>
  <span class="ico" style="left:224px;top:1659px;"></span>
  <span class="t foot" style="left:238px;top:1658px;line-height:1.3;">12 Beispielgasse<br>1010 Musterstadt</span>
  <span class="ico" style="left:224px;top:1681px;"></span>
  <span class="t foot" style="left:238px;top:1682px;">+43 1 000 0000</span>
  <span class="ico" style="left:224px;top:1699px;"></span>
  <span class="t foot" style="left:238px;top:1700px;">hilfe@rendolo-beispiel.at</span>
  <span class="t foot-h" style="left:324px;top:1643px;">Social On</span>
  <span class="box" style="left:324px;top:1657px;width:6px;height:6px;border-radius:50%;background:#777;"></span>
  <span class="box" style="left:334px;top:1657px;width:6px;height:6px;border-radius:50%;background:#777;"></span>
  <span class="box" style="left:344px;top:1657px;width:6px;height:6px;border-radius:50%;background:#777;"></span>
  <div class="store-btn light" style="left:322px;top:1675px;height:14px;"><span class="dot"></span><div><small>Download in</small><strong>AppHafen</strong></div></div>
  <div class="store-btn light" style="left:322px;top:1697px;height:14px;"><span class="dot"></span><div><small>Now In</small><strong>Playmarkt</strong></div></div>
  <span class="t foot" style="left:300px;top:1731px;font-size:3.5px;">Terms and Conditions &nbsp; Privacy Policy &nbsp; Disclaimer</span>
</section>

</body>
</html>
```